Morden, Creative, Unique, Independent Wine Shop

1. We are a brand new wine shop located in Melbourne Australia, we have our logo already, simply use the logo to design a business card.
2. I have uploaded our logo in two versions, with or without shadow, any of them is acceptable.
3. Make it as creative and unique as possible, no limitation of shape, color combination, geometry pattern, fonts, composing etc.
3. Info on the card:
- Brambleford Wine Cellar (Not very necessary if logo is obviously shown)
- 42 Ferncastle Steet, Hampton, Victoria, Australia 3188
- +61 3 9018 4637
- www.bramblefordwinecellar.com.au
- bramblefordwinecellar@mailvista.com
- Additional icons: Google, Instagram, Facebook, Twitter
4. Once again, forget it is a commercial card, make it special.

```html
<!DOCTYPE html>
<html lang="en">
<head>
<meta charset="utf-8">
<title>Brambleford Wine Cellar – Business Card</title>
<link href="https://fonts.googleapis.com/css2?family=Marcellus&family=Lato:wght@400;700&display=swap" rel="stylesheet">
<style>
  :root {
    --backdrop: #d9d9d9;
    --card: #ffffff;
    --wine: #8a1430;
    --ink: #4a4a4a;
    --mark-grey: #6f6f6f;
    --shadow: rgba(0, 0, 0, 0.35);
  }
  * { margin: 0; padding: 0; box-sizing: border-box; }
  html, body {
    width: 1200px;
    height: 802px;
    overflow: hidden;
    background: var(--backdrop);
  }
  .canvas {
    position: relative;
    width: 1200px;
    height: 802px;
  }
  .card {
    position: absolute;
    top: 274px;
    width: 443px;
    height: 260px;
    background: var(--card);
    box-shadow: 0 4px 8px var(--shadow);
    overflow: hidden;
  }
  .card--front { left: 136px; }
  .card--back { left: 624px; }

  .person {
    position: absolute;
    left: 29px;
    top: 34px;
  }
  .person__name {
    font-family: "Marcellus", serif;
    font-size: 19px;
    color: var(--wine);
    letter-spacing: 0.5px;
    line-height: 1;
    text-transform: uppercase;
  }
  .person__role {
    font-family: "Lato", sans-serif;
    font-size: 12.5px;
    color: var(--ink);
    margin-top: 1px;
  }

  .contacts {
    position: absolute;
    left: 29px;
    top: 132px;
    list-style: none;
    font-family: "Lato", sans-serif;
    font-size: 12.5px;
    color: var(--ink);
  }
  .contacts li {
    display: flex;
    align-items: center;
    gap: 5px;
    height: 16px;
  }
  .contacts svg { width: 11px; height: 11px; fill: var(--wine); flex: none; }

  .address {
    position: absolute;
    left: 29px;
    top: 187px;
    font-family: "Lato", sans-serif;
    font-style: normal;
    font-size: 12.5px;
    line-height: 16px;
    color: var(--ink);
  }
  .address__company {
    color: var(--wine);
    text-transform: uppercase;
  }

  .front-emblem {
    position: absolute;
    left: 318px;
    top: 40px;
    width: 110px;
    height: 110px;
    border-radius: 50%;
    background: #ededed;
  }

  .brand {
    position: absolute;
    left: 0;
    right: 0;
    top: 0;
    bottom: 0;
    display: flex;
    align-items: center;
    justify-content: center;
    gap: 12px;
  }
  .brand__dot {
    width: 34px;
    height: 34px;
    border-radius: 50%;
    background: var(--mark-grey);
  }
  .brand__name {
    font-family: "Marcellus", serif;
    font-size: 24px;
    color: var(--wine);
    letter-spacing: 0.5px;
  }
</style>
</head>
<body>
<main class="canvas">

  <section class="card card--front" aria-label="Business card front">
    <div class="person">
      <h1 class="person__name">Daniel Harcourt</h1>
      <p class="person__role">Managing Director</p>
    </div>

    <ul class="contacts">
      <li>
        <svg viewBox="0 0 12 12" aria-hidden="true"><path d="M1 4c0-2 2-3 5-3s5 1 5 3v1H8V4H4v1H1z M2 6h8l1 5H1z"/></svg>
        +61 3 9018 4637
      </li>
      <li>
        <svg viewBox="0 0 12 12" aria-hidden="true"><path d="M0 2h12v8H0z" /><path d="M0 2l6 5 6-5" fill="none" stroke="#fff" stroke-width="1.2"/></svg>
        bramblefordwinecellar@mailvista.com
      </li>
      <li>
        <svg viewBox="0 0 12 12" aria-hidden="true"><circle cx="6" cy="6" r="5.5"/><path d="M3 4c1 0 2 1 2 2s-1 1-1 3M7 2c0 1 1 2 2 2" fill="none" stroke="#fff" stroke-width="1"/></svg>
        www.bramblefordwinecellar.com.au
      </li>
    </ul>

    <address class="address">
      <span class="address__company">Brambleford Wine Cellar</span><br>
      42 Ferncastle Steet, Hampton<br>
      Victoria, Australia 3188
    </address>

    <div class="front-emblem" aria-hidden="true"></div>
  </section>

  <section class="card card--back" aria-label="Business card back">
    <div class="brand">
      <span class="brand__dot" aria-hidden="true"></span>
      <span class="brand__name">Brambleford Wine Cellar</span>
    </div>
  </section>

</main>
</body>
</html>
```